The Harrowgate Ledger Summit. A Summit For Ledger Keepers...By Ledger Keepers.
The Harrowgate Ledger Summit was created to provide quality content at a reasonable price-point to allow organizations to send multiple attendees and encourage active participation. This event is intended for debt collection professionals who are:

Senior Level Executives
Front Line Collection Managers
Compliance Professionals
Trainers
While there are many great conferences within our industry to choose from, most collection conferences just scratch the surface when attempting to provide real world solutions. The Harrowgate Ledger Summit was created to provide debt collection professionals with a foundation of direction, insight, and actionable solutions that can be applied regardless of the size of an organization. Join us at the inaugural Harrowgate Ledger Summit as we assemble an expert team of operations, compliance, and training professionals that will deep dive into real world solutions for today’s real world debt collection issues. Here is what you can expect:

Solution driven sessions, not sponsor driven sessions
Substance from "In The Trenches" experts who live it, breathe it, work it...every day
Learn operational, compliance, and training strategies that have proven success
Understand how to efficiently and effectively manage YOUR resources
Apply state of the art technology solutions

Target Market(s)

Debt collection agencies and creditors

Industry/Entity Type

Financial Service

Font styles to use
Serif

Requirements
Must have
• link to website www.HLS2016.example and use of image provided HLSCover. Use same color scheme as the HLSCover image

```html
<!DOCTYPE html>
<html lang="en">
<head>
<meta charset="utf-8">
<title>Harrowgate Ledger Summit 2016 – Postcard</title>
<link rel="stylesheet" href="https://fonts.googleapis.com/css2?family=Open+Sans:wght@400;600;700&family=Share+Tech+Mono&family=Arimo:wght@400;700&display=swap">
<style>
:root{
  --bg:#ece8e2;
  --teal:#25c6d6;
  --teal-deep:#1b8fa0;
  --lime:#c8d85a;
  --lime-bright:#dbe64a;
  --ink:#1f1f1f;
  --white:#ffffff;
  --gray-dark:#2b2b2b;
  --gray-mid:#7d7d7d;
  --gray-light:#b9b9b9;
}
*{margin:0;padding:0;box-sizing:border-box}
html,body{width:1200px;height:1121px;overflow:hidden;background:var(--bg)}
body{position:relative;font-family:"Open Sans",sans-serif}

/* ---------- front ---------- */
.front{position:absolute;left:40px;top:178px;width:452px;height:628px;overflow:hidden;box-shadow:0 6px 18px rgba(0,0,0,.25)}
.front-photo{position:absolute;inset:0;background:linear-gradient(180deg,var(--gray-mid) 0%,var(--gray-light) 30%,#9a9a9a 55%,#5a5a5a 78%,var(--gray-dark) 100%)}
.front-shapes{position:absolute;inset:0}
.front-social{position:absolute;top:26px;right:34px;display:flex;align-items:center;gap:5px;font-family:"Arimo",sans-serif;font-size:10px;font-weight:700;color:var(--white)}
.front-social .dot{width:9px;height:9px;background:var(--teal)}
.front-brand{position:absolute;left:196px;top:438px;display:flex;gap:12px}
.front-brand .mark{width:26px;height:26px;background:var(--teal);margin-top:6px}
.front-title{font-family:"Share Tech Mono",monospace;font-weight:400;font-size:25px;line-height:37px;letter-spacing:3px;color:var(--white);border-left:1px solid rgba(255,255,255,.6);padding-left:12px}
.front-tagline{position:absolute;left:264px;top:549px;font-family:"Arimo",sans-serif;font-size:7.4px;color:var(--white)}
.front-when{position:absolute;left:264px;top:570px;font-family:"Arimo",sans-serif;font-size:9.4px;font-weight:700;line-height:12px;color:var(--white)}

/* ---------- back ---------- */
.back{position:absolute;left:543px;top:267px;width:628px;height:451px;background:var(--white);overflow:hidden;box-shadow:0 6px 18px rgba(0,0,0,.25)}
.back-art{position:absolute;left:0;top:0}
.back-copy{position:absolute;left:14px;top:20px;width:352px;color:var(--white)}
.back-heading{font-size:15.4px;font-weight:600;line-height:19.5px;text-transform:uppercase}
.back-intro,.back-body{font-size:8.6px;line-height:11.8px;margin-top:4px;text-align:justify}
.back-intro{width:318px}
.back-body{margin-left:3px;margin-top:8px;width:346px}
.audience{list-style:none;display:grid;grid-template-columns:144px 150px;margin:6px 0 0 3px;font-size:8.6px;font-weight:600;row-gap:4px}
.audience li{display:flex;align-items:center;gap:8px}
.audience li::before{content:"";width:0;height:0;border-top:4px solid transparent;border-bottom:4px solid transparent;border-left:8px solid var(--lime-bright)}
.expect{list-style:none;margin:9px 0 0 3px;font-size:8.6px;font-weight:600;line-height:11.8px;width:320px}
.expect li{position:relative;padding-left:15px;margin-bottom:4px}
.expect li::before{content:"";position:absolute;left:0;top:3px;width:6px;height:6px;border-radius:50%;background:var(--lime-bright)}
.contact{position:absolute;left:20px;top:387px;color:var(--white);font-size:9.4px}
.contact h3{font-size:10px;font-weight:600;color:var(--lime-bright);margin-bottom:4px}
.contact-row{display:flex;gap:26px;margin-left:10px;margin-bottom:4px}
.contact-item{display:flex;align-items:center;gap:6px;font-weight:600}
.contact-item svg{flex:none}
.stamp{position:absolute;left:560px;top:23px;width:46px;height:56px;border:1px solid var(--ink)}
.address-line{position:absolute;left:407px;width:198px;height:1px;background:var(--ink)}
</style>
</head>
<body>

<section class="front" aria-label="Postcard front">
  <div class="front-photo" role="img" aria-label="Black and white photo of a riverside city skyline with a tall steel arch"></div>
  <svg class="front-shapes" width="452" height="628" viewBox="0 0 452 628" aria-hidden="true">
    <defs>
      <linearGradient id="wash" x1="0" y1="0" x2="0" y2="1">
        <stop offset="0" stop-color="#25c6d6" stop-opacity=".9"/>
        <stop offset=".55" stop-color="#25c6d6" stop-opacity=".75"/>
        <stop offset=".65" stop-color="#c8d85a" stop-opacity=".8"/>
        <stop offset="1" stop-color="#dbe64a" stop-opacity=".85"/>
      </linearGradient>
    </defs>
    <rect x="0" y="0" width="272" height="628" fill="url(#wash)" opacity=".85"/>
  </svg>
  <div class="front-social"><span class="dot"></span>Connect</div>
  <div class="front-brand">
    <span class="mark"></span>
    <h1 class="front-title">HARROWGATE<br>LEDGER<br>SUMMIT 2016</h1>
  </div>
  <p class="front-tagline">A Summit for ledger keepers... by ledger keepers.</p>
  <p class="front-when">RIVERBEND, MISSOURI<br>MARCH 21, 2016 - MARCH 23, 2016</p>
</section>

<section class="back" aria-label="Postcard back">
  <svg class="back-art" width="390" height="451" viewBox="0 0 390 451">
    <defs>
      <clipPath id="panel">
        <ellipse cx="60" cy="225" rx="318" ry="300"/>
      </clipPath>
      <linearGradient id="water" x1="0" y1="0" x2="0" y2="1">
        <stop offset="0" stop-color="#2aa6b6"/>
        <stop offset=".5" stop-color="#1b8fa0"/>
        <stop offset="1" stop-color="#25a9b9"/>
      </linearGradient>
    </defs>
    <rect x="200" y="0" width="138" height="451" fill="var(--lime)"/>
    <g clip-path="url(#panel)">
      <rect x="0" y="0" width="390" height="451" fill="url(#water)" role="img" aria-label="Teal tinted photo of river water and skyline"/>
      <rect x="0" y="379" width="390" height="72" fill="var(--ink)"/>
    </g>
  </svg>

  <div class="back-copy">
    <h2 class="back-heading">The Harrowgate Ledger Summit<br>A Summit for Ledger Keepers…By<br>Ledger Keepers</h2>
    <p class="back-intro">The Harrowgate Ledger Summit was created to provide quality content at a reasonable price-point to allow organizations to send multiple attendees and encourage active participation. This event is intended for debt collection professionals who are:</p>
    <ul class="audience">
      <li>Senior Level Executives</li>
      <li>Front Line Collection Managers</li>
      <li>Compliance Professionals</li>
      <li>Trainers</li>
    </ul>
    <p class="back-body">While there are many great conferences within our industry to choose from, most collection conferences just scratch the surface when attempting to provide real world solutions. The Harrowgate Ledger Summit was created to provide debt collection professionals with a foundation of direction, insight, and actionable solutions that can be applied regardless of the size of an organization. Join us at the inaugural Harrowgate Ledger Summit as we assemble an expert team of operations, compliance, and training professionals that will deep dive into real world solutions for today’s real world debt collection issues. Here is what you can expect:</p>
    <ul class="expect">
      <li>Solution driven sessions, not sponsor driven sessions</li>
      <li>Substance from "In The Trenches" experts who live it, breathe it, work it… every day</li>
      <li>Learn operational, compliance, and training strategies that have proven results</li>
      <li>Understand how to efficiently and effectively manage YOUR resources</li>
      <li>Apply state of the art technology solutions</li>
    </ul>
  </div>

  <div class="contact">
    <h3>Contact Details</h3>
    <div class="contact-row">
      <span class="contact-item">
        <svg width="8" height="9" viewBox="0 0 8 9"><path d="M1 0.5h2l0.6 2-1.2 0.8c0.4 1.2 1.2 2 2.3 2.4l0.8-1.1 2 0.6v2c-4 0.5-7-2.5-6.5-6.7z" fill="var(--lime-bright)"/></svg>
        555-014-2288
      </span>
      <span class="contact-item">
        <svg width="9" height="9" viewBox="0 0 9 9"><circle cx="4.5" cy="4.5" r="4" fill="none" stroke="var(--lime-bright)"/><path d="M0.5 4.5h8M4.5 0.5v8" stroke="var(--lime-bright)" stroke-width=".8"/></svg>
        www.HLS2016.example
      </span>
    </div>
    <div class="contact-row">
      <span class="contact-item">
        <svg width="9" height="7" viewBox="0 0 9 7"><rect x="0.5" y="0.5" width="8" height="6" fill="var(--lime-bright)"/><path d="M0.5 0.5l4 3.2 4-3.2" fill="none" stroke="var(--ink)" stroke-width=".8"/></svg>
        info@hls2016.example
      </span>
    </div>
  </div>

  <div class="stamp"></div>
  <div class="address-line" style="top:226px"></div>
  <div class="address-line" style="top:262px"></div>
  <div class="address-line" style="top:298px"></div>
</section>

</body>
</html>
```